Modern looking signage for dental office.

Exterior signage for passing cars
Target Market(s)
Cars passing by
Font styles to use
Sans Serif
Colors
3276b5
Requirements
Must have
- Logo
- OPEN ON SUTURDAY AND SUNDAY
- NIGHT CLINIC AVAILABLE
- PLEASE USE THE FONT TYPE IN FILE 4 UPLOADED BELOW.
- (482) 730-2964
- Modern looking

```html
<!DOCTYPE html>
<html lang="en">
<head>
<meta charset="utf-8">
<title>Northvale Dental – Weekend &amp; Night Clinic Sign</title>
<link href="https://fonts.googleapis.com/css2?family=Lato:wght@300;400;700;900&family=Encode+Sans+Condensed:wght@400&display=swap" rel="stylesheet">
<style>
  :root{
    --teal:#0a86a0;
    --ink:#4a4a4d;
    --bar-grey:#5f6063;
    --white:#ffffff;
  }
  *{margin:0;padding:0;box-sizing:border-box}
  html,body{width:1200px;height:1200px;overflow:hidden;background:var(--white)}
  .sign{position:relative;width:1200px;height:1200px;background:var(--white);font-family:"Lato",sans-serif;color:var(--ink)}
  .header-arcs{position:absolute;left:0;top:0}
  .brand-mark{position:absolute;left:152px;top:74px;width:190px;height:190px;border:3px solid var(--ink);border-radius:50%}
  .brand-text{position:absolute;left:366px;top:130px;width:690px;display:flex;flex-direction:column;align-items:center}
  .brand-name{font-weight:300;font-size:70px;letter-spacing:0;line-height:1;color:var(--ink);white-space:nowrap}
  .brand-tagline{font-family:"Encode Sans Condensed",sans-serif;font-weight:400;font-size:42px;line-height:1;margin-top:34px;color:var(--ink);white-space:nowrap}
  .open-word{position:absolute;left:78px;top:470px;font-weight:900;font-size:194px;line-height:1;color:var(--teal);letter-spacing:-2px}
  .open-days{position:absolute;left:620px;top:500px;font-weight:400;font-size:84px;line-height:84px;color:var(--ink);white-space:nowrap}
  .night-bar{position:absolute;left:113px;top:703px;width:974px;height:73px;display:flex;background:var(--bar-grey);color:var(--white);font-weight:700;font-size:46px;align-items:stretch}
  .night-bar span{display:flex;align-items:center;white-space:nowrap}
  .night-bar .lead{padding-left:44px;width:420px}
  .night-bar .hours{background:var(--teal);width:309px;justify-content:center}
  .night-bar .tail{padding-left:8px}
  .contact-panel{position:absolute;left:0;top:834px;width:1200px;height:366px;background:var(--teal)}
  .contact-frame{position:absolute;left:0;top:0}
  .phone-number{position:absolute;left:73px;top:126px;width:1054px;height:159px;display:flex;align-items:center;justify-content:center;font-weight:900;font-size:124px;color:var(--white);letter-spacing:-1px;white-space:nowrap}
  .website{position:absolute;left:0;top:306px;width:1200px;text-align:center;font-size:31px;color:var(--white)}
</style>
</head>
<body>
<main class="sign">
  <svg class="header-arcs" width="1200" height="480" viewBox="0 0 1200 480" aria-hidden="true">
    <path d="M0 136 Q 590 633 1200 226" fill="none" stroke="var(--ink)" stroke-width="3"/>
    <path d="M0 198 Q 590 632 1200 186" fill="none" stroke="var(--teal)" stroke-width="3"/>
  </svg>

  <header class="brand">
    <div class="brand-mark"></div>
    <div class="brand-text">
      <h1 class="brand-name">NORTHVALE DENTAL</h1>
      <p class="brand-tagline">MODERN GENERAL DENTISTRY</p>
    </div>
  </header>

  <h2 class="open-word">OPEN</h2>
  <p class="open-days">on SATURDAY<br>and SUNDAY</p>

  <p class="night-bar">
    <span class="lead">Night clinic from</span>
    <span class="hours">5pm to 10pm</span>
    <span class="tail">available</span>
  </p>

  <section class="contact-panel">
    <svg class="contact-frame" width="1200" height="300" viewBox="0 0 1200 300" aria-hidden="true">
      <path d="M463 126 H103 Q73 126 73 156 V255 Q73 285 103 285 H1097 Q1127 285 1127 255 V156 Q1127 126 1097 126 H620"
            fill="none" stroke="var(--white)" stroke-width="5" stroke-linecap="round"/>
      <circle cx="599" cy="67" r="57" fill="none" stroke="var(--white)" stroke-width="5"/>
      <g fill="var(--white)">
        <path d="M572 48 q6-6 12 0 l8 11 q3 5-1 9 l-5 5 q5 12 18 20 l5-5 q4-4 9-1 l11 8 q6 6 0 12 l-6 6 q-9 7-26-3 q-22-14-32-36 q-6-14 1-21z"/>
      </g>
      <g fill="none" stroke="var(--white)" stroke-width="4" stroke-linecap="round">
        <path d="M602 46 a14 14 0 0 1 14 14"/>
        <path d="M603 35 a25 25 0 0 1 25 25"/>
        <path d="M604 24 a36 36 0 0 1 36 36"/>
      </g>
    </svg>
    <p class="phone-number">(482) 730-2964</p>
    <p class="website">www.northvaledentalclinic.com</p>
  </section>
</main>
</body>
</html>
```